My Billboard for Law Firm

Designing a billboard

Should have
Corvell & Pine, LLC
Ph: 555-214-7390
Auto Accidents / Personal Injury
Family Law
Criminal Defense
Real Estate
Free Consultation

Target Market(s)

Legal

Industry/Entity Type

Legal

Font styles to use
Serif
Sans Serif

Requirements
Must have
• Designing a billboard

Should have
Corvell & Pine, LLC
Ph: 555-214-7390
Family Law
Criminal Defense
Real Estate
Free Consultation
Nice to have
• Nice to have info above
Should not have
• None

```html
<!DOCTYPE html>
<html lang="en">
<head>
<meta charset="utf-8">
<title>Corvell &amp; Pine, LLC Billboard</title>
<link href="https://fonts.googleapis.com/css2?family=EB+Garamond:ital,wght@0,400;0,500;0,700;1,400&display=swap" rel="stylesheet">
<style>
  :root {
    --page-bg: #efece6;
    --sand: #cfbf95;
    --ink-dark: #0b181b;
    --bronze: #8a5a3c;
    --text-dark: #1f1d1a;
    --text-light: #f4efe4;
    --divider: #ffffff;
  }
  html, body {
    margin: 0;
    padding: 0;
    width: 720px;
    height: 1200px;
    overflow: hidden;
    background: var(--page-bg);
  }
  .billboard {
    position: absolute;
    left: 20px;
    top: 430px;
    width: 680px;
    height: 340px;
    box-shadow: 0 10px 24px rgba(0,0,0,0.25);
    font-family: "EB Garamond", Georgia, serif;
  }
  .billboard-shapes {
    position: absolute;
    inset: 0;
    width: 680px;
    height: 340px;
    display: block;
  }
  .firm-name {
    position: absolute;
    left: 35px;
    top: 14px;
    margin: 0;
    font-weight: 400;
    font-size: 33px;
    line-height: 1;
    color: var(--text-dark);
    letter-spacing: 0.2px;
  }
  .attorneys {
    position: absolute;
    left: 38px;
    top: 52px;
    margin: 0;
    font-style: italic;
    font-size: 16px;
    color: var(--text-dark);
  }
  .services {
    position: absolute;
    left: 34px;
    top: 107px;
    margin: 0;
    padding: 0;
    list-style: none;
  }
  .services li {
    display: flex;
    align-items: center;
    height: 24.5px;
    font-size: 19px;
    font-weight: 500;
    color: var(--text-light);
  }
  .services .tick {
    width: 12px;
    height: 12px;
    margin-right: 14px;
    flex: none;
  }
  .phone {
    position: absolute;
    left: 33px;
    top: 271px;
    display: flex;
    align-items: center;
  }
  .phone-icon {
    width: 34px;
    height: 34px;
    margin-right: 9px;
  }
  .phone-number {
    font-size: 42px;
    font-weight: 700;
    color: var(--ink-dark);
    line-height: 1;
  }
</style>
</head>
<body>
  <div class="billboard">
    <svg class="billboard-shapes" viewBox="0 0 680 340" xmlns="http://www.w3.org/2000/svg">
      <defs>
        <linearGradient id="gavel-photo-tone" x1="0" y1="0" x2="1" y2="1">
          <stop offset="0" stop-color="#e6cdb0"/>
          <stop offset="0.5" stop-color="#d2ad8a"/>
          <stop offset="1" stop-color="#a86f4f"/>
        </linearGradient>
        <clipPath id="left-panel-clip">
          <path d="M0 0 H358 L430 140 Q448 170 430 200 L358 340 H0 Z"/>
        </clipPath>
      </defs>
      <rect class="gavel-photo" x="360" y="0" width="320" height="340" fill="url(#gavel-photo-tone)" role="img" aria-label="Photo of a wooden judge's gavel resting on its block"/>
      <polygon class="accent-triangle" points="368,0 450,0 404,64" fill="var(--bronze)"/>
      <polygon class="accent-triangle" points="368,340 450,340 404,276" fill="var(--bronze)"/>
      <path class="divider-curve" d="M0 0 H374 L446 140 Q464 170 446 200 L374 340 H0 Z" fill="var(--divider)"/>
      <g clip-path="url(#left-panel-clip)">
        <rect class="sand-panel" x="0" y="0" width="460" height="340" fill="var(--sand)"/>
        <rect class="service-band" x="0" y="93" width="460" height="152" fill="var(--ink-dark)"/>
      </g>
      <polygon class="band-pointer" points="63,245 81,245 72,256" fill="var(--ink-dark)"/>
    </svg>

    <h1 class="firm-name">Corvell &amp; Pine, LLC</h1>
    <p class="attorneys">Attorneys: Evan Corvell, &amp; Marcus D. Pine</p>

    <ul class="services">
      <li><svg class="tick" viewBox="0 0 12 12"><circle cx="6" cy="6" r="4.8" fill="none" stroke="#f4efe4" stroke-width="1.2"/><path d="M3.6 6.2 L5.4 7.9 L10.5 2.4" fill="none" stroke="#f4efe4" stroke-width="1.3"/></svg>Auto Accidents / Personal Injury</li>
      <li><svg class="tick" viewBox="0 0 12 12"><circle cx="6" cy="6" r="4.8" fill="none" stroke="#f4efe4" stroke-width="1.2"/><path d="M3.6 6.2 L5.4 7.9 L10.5 2.4" fill="none" stroke="#f4efe4" stroke-width="1.3"/></svg>Family Law</li>
      <li><svg class="tick" viewBox="0 0 12 12"><circle cx="6" cy="6" r="4.8" fill="none" stroke="#f4efe4" stroke-width="1.2"/><path d="M3.6 6.2 L5.4 7.9 L10.5 2.4" fill="none" stroke="#f4efe4" stroke-width="1.3"/></svg>Criminal Defense</li>
      <li><svg class="tick" viewBox="0 0 12 12"><circle cx="6" cy="6" r="4.8" fill="none" stroke="#f4efe4" stroke-width="1.2"/><path d="M3.6 6.2 L5.4 7.9 L10.5 2.4" fill="none" stroke="#f4efe4" stroke-width="1.3"/></svg>Real Estate</li>
      <li><svg class="tick" viewBox="0 0 12 12"><circle cx="6" cy="6" r="4.8" fill="none" stroke="#f4efe4" stroke-width="1.2"/><path d="M3.6 6.2 L5.4 7.9 L10.5 2.4" fill="none" stroke="#f4efe4" stroke-width="1.3"/></svg>Free Consultation</li>
    </ul>

    <div class="phone">
      <svg class="phone-icon" viewBox="0 0 34 34">
        <circle cx="17" cy="17" r="16" fill="var(--bronze)" stroke="#ffffff" stroke-width="2"/>
        <path d="M11.5 9.5 L14.5 9 L16 13 L14 14.6 Q15.5 18.5 19.4 20 L21 18 L25 19.5 L24.5 22.5 Q22.5 25 19.5 24 Q11 21 10 14.5 Q9.5 11 11.5 9.5 Z" fill="#ffffff"/>
        <path d="M19 10.5 Q23 11 23.5 15" fill="none" stroke="#ffffff" stroke-width="1.4"/>
        <path d="M19 7.5 Q26 8 26.5 15" fill="none" stroke="#ffffff" stroke-width="1.4"/>
      </svg>
      <span class="phone-number">555-214-7390</span>
    </div>
  </div>
</body>
</html>
```